Direct to Consumer extended service contract business with a new disruptive business model needs a

We need a customized wordpress design for a company called 'Tall Harbor Assurance'.
We provide an innovative and unique service contract protection program direct to consumers. This program provides monthly coverage for all electronics purchased in the last 4 years and all electronics the consumer purchases in the future for a low monthly fee. The overall design should communicate a sense of legitimacy, ethics, and superior customer service and support (in an industry that has a huge PR issue to overcome).
Electronics is the first product group, other product groups with different price points to launch in the future..

Target Market(s)

All purchasers of electronic goods...all demographics

Industry/Entity Type

Electronics

Font styles to use
Sans Serif

Requirements
Must have
• Customer Testimonials
Industry News
Customer ratings
Blog posts
Call to action messaging
Like the functional elements and design of bramblequill.example (need to be better)
Nice to have
• Like to see video testimonials
Social network "whats trending related to electronics or service contract industry"
Easy way to register products for warranty

```html
<!DOCTYPE html>
<html lang="en">
<head>
<meta charset="utf-8">
<title>Tall Harbor Assurance</title>
<link href="https://fonts.googleapis.com/css2?family=Open+Sans:wght@400;600;700&family=Oswald:wght@300;400&display=swap" rel="stylesheet">
<style>
:root{
  --blue:#00a3e8;
  --blue-dark:#0088c9;
  --navy:#2c3e50;
  --ink:#333;
  --muted:#777;
  --topbar:#2b3a44;
  --pale:#e8f6fb;
  --grey-band:#f4f5f6;
  --red:#e8141b;
  --white:#fff;
}
*{box-sizing:border-box;margin:0;padding:0}
html,body{width:1200px;height:2726px;overflow:hidden}
body{font-family:"Open Sans",Arial,sans-serif;color:var(--ink);background:var(--white);position:relative;font-size:12px}
h2,.heading{font-family:"Oswald",Arial,sans-serif;font-weight:400}

.topbar{position:absolute;top:0;left:0;width:1200px;height:26px;background:var(--topbar);color:#dfe6ea;font-size:10px;font-weight:600}
.topbar .links{position:absolute;top:7px;display:flex;gap:10px}
.topbar .left{left:165px}.topbar .right{right:200px}

.header{position:absolute;top:26px;left:0;width:1200px;height:129px}
.logo{position:absolute;left:176px;top:38px;display:flex;align-items:center;gap:10px;font-weight:700;font-size:30px;color:var(--navy);letter-spacing:.5px;line-height:1}
.logo .mark{width:26px;height:26px;background:var(--blue)}
.social{position:absolute;left:812px;top:18px;display:flex;gap:8px}
.social span{width:30px;height:30px;border-radius:50%;background:var(--navy)}
.search{position:absolute;left:760px;top:78px;width:238px;height:32px;border:1px solid #cfd8dd;font-size:10px;color:#aaa;padding:9px 10px}
.search svg{position:absolute;right:6px;top:5px}

.nav{position:absolute;top:155px;left:0;width:1200px;height:41px;background:linear-gradient(#1cb6f0,var(--blue-dark));color:var(--white);font-size:12px}
.nav ul{list-style:none;position:absolute;left:178px;top:12px;display:flex;gap:30px}
.dropdown{position:absolute;left:935px;top:202px;width:187px;background:linear-gradient(#35bff2,#1aa8e0);color:var(--white);font-size:11px;z-index:3}
.dropdown li{list-style:none;padding:9px 14px;border-bottom:1px solid rgba(255,255,255,.35)}

.hero{position:absolute;top:196px;left:0;width:1200px;height:464px;background:var(--pale)}
.hero-frame{position:absolute;left:159px;top:6px;width:846px;height:448px;background:#f6fbfd;border:6px solid #dcf0f8}
.hero h1{position:absolute;top:42px;width:100%;text-align:center;font-family:"Oswald",Arial,sans-serif;font-weight:400;font-size:30px;color:var(--blue-dark)}
.hero .sub{position:absolute;top:82px;width:100%;text-align:center;font-size:17px;color:#555;font-family:"Oswald",Arial,sans-serif;font-weight:300}
.device-art{position:absolute;left:30px;top:116px;width:420px;height:265px;background:linear-gradient(135deg,#3a3f48,#7fa6cf 55%,#2a2e35);border-radius:8px}
.quote{position:absolute;left:508px;top:141px;width:307px;height:246px;background:#e3f1f7;padding:22px 24px}
.quote h3{font-family:"Oswald",Arial,sans-serif;font-weight:400;font-size:19px;text-align:center;color:#333;margin-bottom:18px}
.quote .field{height:32px;background:var(--white);border:1px solid #ccc;font-size:11px;color:#666;padding:8px 10px;margin-bottom:14px;position:relative}
.quote .field::after{content:"";position:absolute;right:10px;top:13px;border:5px solid transparent;border-top-color:#666}
.quote .cta{height:36px;background:var(--red);color:var(--white);font-size:11px;font-weight:700;text-align:center;padding-top:11px}
.arrow{position:absolute;top:404px;width:56px;height:56px}
.arrow.prev{left:88px}.arrow.next{left:1016px}

.rated{position:absolute;top:682px;width:1200px;text-align:center;font-family:"Oswald",Arial,sans-serif;font-weight:300;font-size:20px;color:var(--blue-dark)}
.rated b{font-weight:400}
.ratings{position:absolute;top:742px;left:165px;width:832px;display:flex;justify-content:space-between}
.rating{width:188px;height:138px;background:var(--blue);color:var(--white);text-align:center;padding-top:12px;border-radius:3px}
.rating .stars{display:flex;justify-content:center;gap:6px;height:26px}
.rating .name{font-size:20px;margin-top:12px}
.rating .meta{font-size:9px}
.rating .more{font-size:10px;margin-top:14px}
.badge-row{display:flex;justify-content:center;gap:10px;height:38px}
.badge-row span{background:var(--white);display:block}

.popular{position:absolute;top:916px;left:0;width:1200px;height:429px;background:var(--grey-band)}
.popular h2,.testimonials h2,.news h2{font-size:21px;color:#333}
.popular h2{position:absolute;top:22px;left:168px}
.pager{position:absolute;left:947px;top:24px;display:flex;gap:2px}
.pager span{width:20px;height:24px;background:#ddd;border:1px solid #ccc}
.cards{position:absolute;top:68px;left:168px;width:815px;display:flex;justify-content:space-between}
.card{width:180px;height:314px;background:var(--white);border:1px solid #e2e2e2;position:relative}
.card .photo{margin:8px;height:200px;border:1px solid #ddd}
.card .title{font-size:11px;font-weight:700;text-align:center;margin-top:6px}
.card .plan{font-size:10px;text-align:center;color:var(--muted)}
.card .price{position:absolute;left:8px;bottom:30px;font-size:10px;color:#555}
.card .read{position:absolute;right:6px;bottom:24px;background:var(--red);color:var(--white);font-size:10px;font-weight:700;padding:5px 8px}
.see-all{position:absolute;top:395px;left:845px;font-size:11px;color:var(--red)}
.rule{position:absolute;top:404px;left:168px;width:665px;border-top:1px dotted #bbb}

.testimonials{position:absolute;top:1345px;left:0;width:1200px;height:390px}
.testimonials h2{position:absolute;top:20px;left:168px}
.more-btn{position:absolute;top:16px;left:845px;background:var(--blue);color:var(--white);font-size:11px;font-weight:600;padding:7px 12px}
.quotes{position:absolute;top:62px;left:168px;width:288px}
.quotes p{font-size:11px;line-height:16px;color:#444;padding-bottom:8px;border-bottom:1px dashed #999}
.quotes .who{font-size:10.5px;font-weight:600;margin:12px 0 16px}
.videos{position:absolute;top:78px;left:500px;width:494px;display:grid;grid-template-columns:238px 238px;gap:20px 18px}
.video{height:119px;position:relative}
.video svg{position:absolute;left:99px;top:44px}

.news{position:absolute;top:1735px;left:0;width:1200px;height:437px;background:var(--grey-band)}
.news h2{position:absolute;top:24px}
.col{position:absolute;top:66px;width:410px}
.item{display:flex;gap:12px;height:83px;border-bottom:1px dashed #888;padding-top:8px}
.item p{font-size:11px;line-height:16px;color:#444}
.date{width:64px;height:64px;background:var(--blue);color:var(--white);text-align:center;flex:none}
.date b{display:block;font-size:28px;line-height:38px;font-weight:600}
.date span{display:block;font-size:10px;border-top:1px solid rgba(255,255,255,.6);margin:0 4px}
.avatar{width:62px;height:62px;flex:none;background:linear-gradient(135deg,#e9c57a,#c98c5a)}

.newsletter{position:absolute;top:2172px;left:0;width:1200px;height:111px}
.newsletter h2{position:absolute;left:178px;top:36px;font-size:22px;color:#333}
.newsletter p{position:absolute;left:398px;top:32px;width:250px;font-size:11px;line-height:16px;color:#444}
.newsletter .email{position:absolute;left:664px;top:37px;width:172px;height:33px;border:1px solid #ccc;font-size:9px;color:#aaa;padding:10px}
.newsletter .go{position:absolute;left:836px;top:37px;width:138px;height:33px;background:var(--blue);color:var(--white);font-size:12px;font-weight:700;padding:9px 16px}

.footer{position:absolute;top:2283px;left:0;width:1200px;height:351px;background:var(--blue);color:var(--white)}
.fcol{position:absolute;top:20px;font-size:10px;line-height:21.5px}
.fcol h4{font-size:12.5px;font-weight:600;line-height:22px}

.bottom{position:absolute;top:2634px;left:0;width:1200px;height:92px}
.fsocial{position:absolute;left:176px;top:14px;display:flex;gap:16px}
.fsocial span{width:24px;height:24px;background:var(--blue);border-radius:50%}
.copy{position:absolute;left:180px;top:64px;font-size:10px;color:#444}
.seals{position:absolute;left:710px;top:10px;display:flex;gap:10px}
.seals span{width:84px;height:40px;background:#d9e1e6;border-radius:4px}
</style>
</head>
<body>

<div class="topbar">
  <div class="links left"><span>1-800-555-0142</span><span>|</span><span>About Us</span><span>|</span><span>Contact Us</span><span>|</span><span>Support</span></div>
  <div class="links right"><span>Set Your Location</span><span>|</span><span>Select Language</span><span>|</span><span>Sign Up</span><span>|</span><span>Log In</span></div>
</div>

<header class="header">
  <div class="logo"><span class="mark"></span>Tall Harbor Assurance</div>
  <div class="social"><span></span><span></span><span></span><span></span><span></span></div>
  <div class="search">Search your plan
    <svg width="24" height="22" viewBox="0 0 24 22"><circle cx="9" cy="9" r="6.5" fill="none" stroke="#2c3e50" stroke-width="2"/><line x1="14" y1="14" x2="21" y2="20" stroke="#2c3e50" stroke-width="3"/></svg>
  </div>
</header>

<nav class="nav">
  <ul><li>Pocketphone</li><li>Slate Tablets</li><li>eBook Readers</li><li>Cameras</li><li>Laptops</li><li>Desktops</li><li>Smartphones</li><li>Television</li><li>Music Systems</li><li>All Plans &#9662;</li></ul>
</nav>
<ul class="dropdown"><li>Plan A</li><li>Plan B</li></ul>

<section class="hero">
  <div class="hero-frame">
    <h1>PROTECT YOUR Slate/Pocketphone FOR $5 A MONTH OR LESS.</h1>
    <div class="sub">save up to 40% vs. your current tablet/Smartphone insurance.</div>
    <div class="device-art" role="img" aria-label="Tablet and smartphone shown side by side"></div>
    <div class="quote">
      <h3>GET A QUOTE TODAY!</h3>
      <div class="field">What product do you have?</div>
      <div class="field">Where did you buy it?</div>
      <div class="cta">GET A QUOTE</div>
    </div>
  </div>
  <svg class="arrow prev" viewBox="0 0 56 56"><circle cx="28" cy="28" r="25" fill="#fff" stroke="#888" stroke-width="4"/><polyline points="32,16 20,28 32,40" fill="none" stroke="#888" stroke-width="5"/></svg>
  <svg class="arrow next" viewBox="0 0 56 56"><circle cx="28" cy="28" r="25" fill="#fff" stroke="#888" stroke-width="4"/><polyline points="24,16 36,28 24,40" fill="none" stroke="#888" stroke-width="5"/></svg>
</section>

<div class="rated">Rated #1 by the people who matter most: <b>Our Clients</b></div>
<section class="ratings">
  <div class="rating">
    <div class="stars"><svg width="150" height="24" viewBox="0 0 150 24" fill="#fff"><g id="st"><polygon points="12,1 15,9 23,9 17,14 19,23 12,18 5,23 7,14 1,9 9,9"/></g><use href="#st" x="31"/><use href="#st" x="62"/><use href="#st" x="93"/><use href="#st" x="124"/></svg></div>
    <div class="name">Appvale Store</div><div class="meta">4.5 average on 7000+ reviews</div><div class="more">Read the reviews ›</div>
  </div>
  <div class="rating">
    <div class="stars"><svg width="150" height="24" viewBox="0 0 150 24" fill="#fff"><use href="#st"/><use href="#st" x="31"/><use href="#st" x="62"/><use href="#st" x="93"/><use href="#st" x="124"/></svg></div>
    <div class="name">Rivermart</div><div class="meta">4.7 average on 35,000+ reviews</div><div class="more">Read the reviews ›</div>
  </div>
  <div class="rating">
    <div class="stars"><svg width="150" height="24" viewBox="0 0 150 24" fill="#fff"><use href="#st"/><use href="#st" x="31"/><use href="#st" x="62"/><use href="#st" x="93"/><use href="#st" x="124"/></svg></div>
    <div class="name">Searchly</div><div class="meta">4.9 average on 600+ reviews</div><div class="more">Read the reviews ›</div>
  </div>
  <div class="rating">
    <div class="badge-row"><span style="width:86px"></span><span style="width:40px"></span></div>
    <div class="name" style="margin-top:0">Fair Trade Bureau</div><div class="meta">with an A+ Rating</div><div class="more">Read the reviews ›</div>
  </div>
</section>

<section class="popular">
  <h2>Popular Plans for Your Products.</h2>
  <div class="pager"><span></span><span></span></div>
  <div class="cards">
    <div class="card"><div class="photo" role="img" aria-label="Black laptop computer" style="background:linear-gradient(#f7f7f7,#cfd3d6)"></div><div class="title">Delmar Notebook 15 R</div><div class="plan">Plan # 24132</div><div class="price">price-$125/year</div><div class="read">Read More ›</div></div>
    <div class="card"><div class="photo" role="img" aria-label="Black digital SLR camera" style="background:linear-gradient(#f7f7f7,#c9cbcd)"></div><div class="title">Sorano Prism DSLR</div><div class="plan">Plan # 24156</div><div class="price">price-$25/year</div><div class="read">Read More ›</div></div>
    <div class="card"><div class="photo" role="img" aria-label="Flat screen television" style="background:linear-gradient(#f7f7f7,#9fb2c8)"></div><div class="title">Sorano Prism DSLR</div><div class="plan">Plan # 24172</div><div class="price">price-$125/year</div><div class="read">Read More ›</div></div>
    <div class="card"><div class="photo" role="img" aria-label="Tablet computer" style="background:linear-gradient(#f7f7f7,#b6c4d3)"></div><div class="title">Orchard Slate</div><div class="plan">Plan # 24189</div><div class="price">price-$25/year</div><div class="read">Read More ›</div></div>
  </div>
  <div class="rule"></div>
  <div class="see-all">See All Popular Plans ›</div>
</section>

<section class="testimonials">
  <h2>What client says about our service?</h2>
  <div class="more-btn">See More Testimonials ›</div>
  <div class="quotes">
    <p>Lorem ipsum dolor sit amet, consectetur adipiscing elit. Sed ante enim, semper at dictum vitae, tristique nec eros. Vivamus tincidunt non risus in pulvinar.</p>
    <div class="who">Owen Carraway, Smart Phone Users, USA</div>
    <p>Lorem ipsum dolor sit amet, consectetur adipiscing elit. Sed ante enim, semper at dictum vitae, tristique nec eros. Vivamus tincidunt non risus in pulvinar.</p>
    <div class="who">Owen Carraway, Smart Phone Users, USA</div>
    <p>Lorem ipsum dolor sit amet, consectetur adipiscing elit. Sed ante enim, semper at dictum vitae, tristique nec eros. Vivamus tincidunt non risus in pulvinar.</p>
    <div class="who">Owen Carraway, Smart Phone Users, USA</div>
  </div>
  <div class="videos">
    <div class="video" role="img" aria-label="Video testimonial from a happy customer" style="background:linear-gradient(135deg,#d9c3ad,#8aa0b4)"><svg width="40" height="30"><rect width="40" height="30" rx="4" fill="#222"/><polygon points="15,8 28,15 15,22" fill="#fff"/></svg></div>
    <div class="video" role="img" aria-label="Video testimonial from a customer using a tablet outdoors" style="background:linear-gradient(135deg,#a8c86a,#d8b890)"><svg width="40" height="30"><rect width="40" height="30" rx="4" fill="#222"/><polygon points="15,8 28,15 15,22" fill="#fff"/></svg></div>
    <div class="video" role="img" aria-label="Video testimonial from a group of customers" style="background:linear-gradient(135deg,#e6d4c2,#9f7f68)"><svg width="40" height="30"><rect width="40" height="30" rx="4" fill="#222"/><polygon points="15,8 28,15 15,22" fill="#fff"/></svg></div>
    <div class="video" role="img" aria-label="Video testimonial from a shopper in a store" style="background:linear-gradient(135deg,#c7b7b0,#e0a9b4)"><svg width="40" height="30"><rect width="40" height="30" rx="4" fill="#222"/><polygon points="15,8 28,15 15,22" fill="#fff"/></svg></div>
  </div>
</section>

<section class="news">
  <h2 style="left:168px">Industry News</h2>
  <h2 style="left:610px">Latest Post from our Blog</h2>
  <div class="col" style="left:168px">
    <div class="item"><div class="date"><b>14</b><span>Sept, 2014</span></div><p>Lorem ipsum dolor sit amet, consectetur adipiscing elit. Sed ante enim, semper at dictum vitae, tristique nec eros. Vivamus tincid unt non risus in pulvinar.</p></div>
    <div class="item"><div class="date"><b>14</b><span>Sept, 2014</span></div><p>Lorem ipsum dolor sit amet, consectetur adipiscing elit. Sed ante enim, semper at dictum vitae, tristique nec eros. Vivamus tincid unt non risus in pulvinar.</p></div>
    <div class="item"><div class="date"><b>14</b><span>Sept, 2014</span></div><p>Lorem ipsum dolor sit amet, consectetur adipiscing elit. Sed ante enim, semper at dictum vitae, tristique nec eros. Vivamus tincid unt non risus in pulvinar.</p></div>
    <div class="item"><div class="date"><b>14</b><span>Sept, 2014</span></div><p>Lorem ipsum dolor sit amet, consectetur adipiscing elit. Sed ante enim, semper at dictum vitae, tristique nec eros. Vivamus tincid unt non risus in pulvinar.</p></div>
  </div>
  <div class="col" style="left:612px;width:380px">
    <div class="item"><div class="avatar" role="img" aria-label="Blog author portrait"></div><p>Lorem ipsum dolor sit amet, consectetur adipiscing elit. Sed ante enim, semper at dictum vitae, tristique nec eros. Vivamus tincid unt non risus in pulvinar.</p></div>
    <div class="item"><div class="avatar" role="img" aria-label="Blog author portrait"></div><p>Lorem ipsum dolor sit amet, consectetur adipiscing elit. Sed ante enim, semper at dictum vitae, tristique nec eros. Vivamus tincid unt non risus in pulvinar.</p></div>
    <div class="item"><div class="avatar" role="img" aria-label="Blog author portrait"></div><p>Lorem ipsum dolor sit amet, consectetur adipiscing elit. Sed ante enim, semper at dictum vitae, tristique nec eros. Vivamus tincid unt non risus in pulvinar.</p></div>
    <div class="item"><div class="avatar" role="img" aria-label="Blog author portrait"></div><p>Lorem ipsum dolor sit amet, consectetur adipiscing elit. Sed ante enim, semper at dictum vitae, tristique nec eros. Vivamus tincid unt non risus in pulvinar.</p></div>
  </div>
</section>

<section class="newsletter">
  <h2>Subscribe Newsletter</h2>
  <p>To get our monthly news, updates about new house and new landscape plans subscribe us</p>
  <div class="email">Type your email id</div>
  <div class="go">Subscribe Now ›</div>
</section>

<footer class="footer">
  <div class="fcol" style="left:170px"><h4>Protection Plans</h4><div>Smartphones</div><div>Pocketphone Warranty</div><div>Galaxia Warranty</div><div>Hexa One Warranty</div><div>Novex Warranty</div><div>Dryad Warranty</div><div>Other Smartphone</div><div>Tablets</div><div>Slate Warranty</div><div>Galaxia Warranty</div><div>Novex Warranty</div><div>Microvale Panel Warranty</div><div>Other Tablet/eReader</div></div>
  <div class="fcol" style="left:342px"><h4>Desktop Computers</h4><div>Orchard Desk Warranty</div><div>Other Desktop Computer</div><h4>Laptops</h4><div>Orchard Book Warranty</div><div>Chromaline Book Warranty</div><div>Delmar Laptop Warranty</div><div>Other Laptop</div><h4>Portable Audio</h4><div>Orchard Player Touch Warranty</div><div>MP3 Player Warranty</div><div>Headphones</div></div>
  <div class="fcol" style="left:521px"><h4>Home Entertainment</h4><div>TV Warranty</div><div>Video Game Warranty</div><div>Sound Bar Warranty</div><div>Other Home Entertainment</div><h4>Home Appliances</h4><div>Dishwasher Warranty</div><div>Refrigerator Warranty</div><div>Washer/Dryer Warranty</div><h4>Other Appliance</h4><div>Other Items</div><div>Camera Warranty</div><div>GPS Warranty</div></div>
  <div class="fcol" style="left:697px"><h4>Site Links</h4><div>My Profile</div><div>Register Plan</div><div>Our Coverage</div><div>Bramblequill Rewards</div><div>Tech Support</div><div>Bidbay Merchant Program</div><div>Business &amp; Education</div><div>Legal Notices</div><div>FAQs &amp; Support</div><div>How-To Videos</div><div>Privacy Policy</div><div>Site Map</div></div>
  <div class="fcol" style="left:857px"><h4>Who We Are</h4><div>About Us</div><div>Leadership</div><div>Bramblequill Promise</div><div>Jobs</div><div>News &amp; Awards</div><div>Press Releases</div><div>Contact Us</div><div>Research Studies</div><div>Drop Tests</div></div>
</footer>

<div class="bottom">
  <div class="fsocial"><span></span><span></span><span></span><span></span><span></span></div>
  <div class="copy">© 2014, All Rights Reserved, Tall Harbor Assurance</div>
  <div class="seals"><span></span><span></span><span></span></div>
</div>

</body>
</html>
```